Marguerite's Stone Hearth Trattoria Pitch Deck

Clean and Minimalist Layout: Use a clean and uncluttered layout with ample white space to enhance readability and focus on the key content.

Color Palette: Choose a color scheme that aligns with your brand identity. Black and White. Opt for a combination of complementary colors to create a visually appealing and cohesive look throughout the presentation.

Typography: Select modern and legible fonts for headings and body text. Consider using a combination of serif and sans-serif fonts to create contrast and hierarchy.

High-Quality Images: Incorporate high-resolution images that visually represent your pizzeria, food offerings, and brand. Ensure the images are clear, well-lit, and of professional quality.

Graphs and Charts: Utilize visually appealing graphs and charts to present financial projections, market data, and growth metrics. Choose appropriate chart types, such as bar graphs or line charts, to effectively communicate data.

Iconography: Include relevant icons and symbols to enhance visual interest and provide quick visual cues. Use them to represent different sections, services, or key points in your presentation.

Slide Transitions and Animations: Use subtle slide transitions and animations to add a touch of interactivity and engage your audience. However, avoid overusing flashy animations that may distract from the content.

Consistent Branding: Ensure that your pitch deck maintains consistent branding elements throughout, such as your logo, color scheme, and typography. This helps to reinforce your brand identity and create a cohesive presentation.

Remember, the goal is to create a visually appealing and professional pitch deck that effectively communicates your key messages. Use visuals, graphs, and design elements strategically to enhance understanding and engagement with your audience.

Target Market(s)

Investors

Industry/Entity Type

Food Industry

Font styles to use
Serif

Colors

Designer to choose only greyscale colors for use in the design.

Requirements
Must have
• Modern and Professional Look: Opt for a modern design that reflects the professional nature of your business. Use clean lines, contemporary fonts, and a visually appealing color scheme to create a polished and professional appearance. Consistent Branding: Incorporate your pizzeria's branding elements such as the logo, colors, and typography throughout the pitch deck. Consistency in branding helps to establish a cohesive and memorable visual identity. Visual Hierarchy: Use visual hierarchy to guide the viewer's attention and emphasize important information. Utilize font sizes, colors, and formatting techniques such as bold and italics to differentiate headings, subheadings, and body text. Engaging Visuals: Incorporate relevant and eye-catching visuals such as high-quality images, graphics, and icons. Visuals should support your content and help communicate your message effectively. Well-Structured Layout: Organize your content into sections and use clear headings and subheadings to create a logical flow. Ensure that each slide has enough white space for readability and avoid cluttered designs. Legible Fonts: Choose fonts that are easy to read on both computer screens and projection screens. Stick to a maximum of two font styles to maintain a clean and professional look. Charts and Graphs: When presenting data or statistics, use charts, graphs, and infographics to present information visually. This makes complex information more digestible and visually appealing. Slide Transitions and Animations: Use slide transitions and subtle animations to enhance the visual experience. However, avoid excessive animations that can distract from your content. Balance of Text and Visuals: Strike a balance between text and visuals. Avoid overcrowding slides with excessive text and focus on presenting key points in a concise and visually appealing manner. Relevance to Content: Ensure that the design elements align with and enhance the content of your pitch deck. Avoid using decorative elements that do not serve a purpose or distract from the main message. Remember, the design should complement and support your content rather than overpowering it. A well-designed pitch deck will capture attention, convey professionalism, and enhance the overall impact of your presentation.

```html
<!DOCTYPE html>
<html lang="en">
<head>
<meta charset="utf-8">
<title>Marguerite's Stone Hearth Trattoria – Pitch Deck</title>
<link href="https://fonts.googleapis.com/css2?family=Noto+Sans:ital,wght@0,400;0,600;0,700;1,400&family=Open+Sans:wght@400;600&display=swap" rel="stylesheet">
<style>
:root{
  --board:#e6e7eb;
  --navy:#0c1d48;
  --navy-2:#0e2770;
  --ink:#1b2236;
  --muted:#6b7080;
  --white:#ffffff;
  --mist-top:#b7bac6;
  --mist-bottom:#eef0f8;
  --gold:#e9b53a;
  --cream:#f7eeb8;
}
*{box-sizing:border-box;margin:0;padding:0}
html,body{width:1200px;height:733px;overflow:hidden}
body{background:linear-gradient(180deg,#f1f2f5,var(--board));font-family:"Noto Sans",sans-serif;color:var(--ink);position:relative}
.slide{position:absolute;width:347px;height:193px;background:var(--white);overflow:hidden;box-shadow:0 6px 16px rgba(20,25,45,.16)}
.c1{left:53px}.c2{left:423px}.c3{left:793px}
.r1{top:50px}.r2{top:266px}.r3{top:482px}
.abs{position:absolute}
.photo{position:absolute}

/* cover slides */
.cover{text-align:center}
.cover--dark{background:#161a27;color:var(--white)}
.cover--dark .photo{inset:0;background:
  radial-gradient(ellipse 120px 60px at 55% 70%,rgba(150,115,60,.45),rgba(0,0,0,0) 100%),
  linear-gradient(180deg,#1d2130,#12151f)}
.cover--light{background:linear-gradient(180deg,var(--mist-top),var(--mist-bottom));color:var(--navy)}
.brand-mark{position:absolute;display:flex;align-items:center;gap:4px;font-weight:700;font-size:9px;letter-spacing:.2px}
.brand-mark i{display:block;width:9px;height:9px;border-radius:50%;border:1.2px solid currentColor}
.cover-title{position:absolute;left:0;right:0;top:84px;font-weight:700;font-size:11.5px}
.person{position:absolute;top:121px;width:120px;text-align:center}
.person b{display:block;font-size:7.2px;font-weight:700}
.person span{display:block;font-size:5.3px;margin-top:1px}
.person em{display:block;font-style:normal;font-size:4.6px;margin-top:8px;opacity:.8}
.cover-date{position:absolute;left:16px;top:175px;font-size:5px}
.cover-site{position:absolute;right:17px;top:175px;font-size:5px}

/* content slides */
.rule{position:absolute;height:1.2px;width:16px;background:var(--navy)}
.h-title{position:absolute;font-weight:700;color:var(--navy);font-size:11.5px;line-height:1.2}
.body-text{font-family:"Open Sans",sans-serif;font-size:3.6px;line-height:1.9;color:var(--muted)}
.footer-brand{position:absolute;left:5px;bottom:2px;font-size:5.2px;line-height:8px;font-weight:700;color:var(--navy);white-space:nowrap}
.footer-bar{position:absolute;left:42px;right:0;bottom:2px;height:8px;background:var(--navy);color:var(--white);font-size:4.6px;display:flex;align-items:center;justify-content:space-between;padding:0 12px 0 104px}
.footer-edge{position:absolute;left:0;bottom:2px;width:2px;height:8px;background:var(--navy)}

.stat{position:absolute;text-align:center}
.stat b{display:block;font-size:8px;font-weight:700;color:var(--navy)}
.stat span{display:block;font-size:4.4px;color:var(--muted);margin-top:2px}
.stat--navy{background:var(--navy)}
.stat--navy b,.stat--navy span{color:var(--white)}
.stat--card{background:var(--white);box-shadow:0 2px 6px rgba(20,25,45,.16)}

.vision-box{position:absolute;left:43px;top:56px;width:261px;height:91px;background:linear-gradient(135deg,var(--navy),var(--navy-2));box-shadow:0 3px 8px rgba(12,29,72,.35);color:var(--white);font-style:italic;font-size:8px;line-height:1.75;text-align:center;display:flex;align-items:center;justify-content:center;padding:0 36px}
.mission-text{position:absolute;left:40px;right:40px;top:73px;text-align:center;font-size:6.6px;line-height:1.75;color:var(--navy);font-weight:400}

.card{position:absolute;background:var(--white);box-shadow:0 2px 7px rgba(20,25,45,.13);border-radius:2px}
.list-item{margin-bottom:6px}
.list-item h4{font-size:4.2px;font-weight:600;color:var(--ink);margin-bottom:1px}
.list-item h4::before{content:"";display:inline-block;width:2px;height:2px;border:.5px solid var(--muted);border-radius:50%;margin-right:3px;vertical-align:middle}
.list-item p{padding-left:6px}
.sq h4::before{border-radius:0;background:var(--navy);border:none}
.icon-dot{position:absolute;width:20px;height:20px;border-radius:50%;background:linear-gradient(135deg,#3a4160,var(--navy));box-shadow:0 2px 5px rgba(12,29,72,.3);display:flex;align-items:center;justify-content:center}
.sub{font-size:5.4px;font-weight:600;color:var(--ink);margin-bottom:3px}
</style>
</head>
<body>

<!-- Row 1: covers -->
<section class="slide c1 r1 cover cover--dark">
  <div class="photo" role="img" aria-label="Dimmed photo of a pizza coming out of a brick oven"></div>
  <div class="brand-mark" style="left:128px;top:46px;color:var(--white)"><i></i>Marguerite's</div>
  <h1 class="cover-title">Marguerite's Stone Hearth Trattoria</h1>
  <div class="person" style="left:52px"><b>Paolo Ferrante</b><span>Owner &amp; CEO</span><em>paolo@margueritestrattoria.com</em></div>
  <div class="person" style="left:159px"><b>Marco Bellini</b><span>Owner, Silent Partner</span><em>marco@margueritestrattoria.com</em></div>
  <p class="cover-date">May 2023</p>
  <p class="cover-site">margueritestrattoria.com</p>
</section>

<section class="slide c2 r1 cover cover--light">
  <div class="brand-mark" style="left:128px;top:46px"><i></i>Marguerite's</div>
  <h1 class="cover-title">Marguerite's Stone Hearth Trattoria</h1>
  <div class="person" style="left:52px"><b>Paolo Ferrante</b><span>Owner &amp; CEO</span><em>paolo@margueritestrattoria.com</em></div>
  <div class="person" style="left:159px"><b>Marco Bellini</b><span>Owner, Silent Partner</span><em>marco@margueritestrattoria.com</em></div>
  <p class="cover-date">May 2023</p>
  <p class="cover-site">margueritestrattoria.com</p>
</section>

<section class="slide c3 r1 cover cover--light" style="text-align:left">
  <div class="brand-mark" style="left:26px;top:56px"><i></i>Marguerite's</div>
  <h1 class="cover-title" style="left:24px;top:92px;font-size:10.5px">Marguerite's Stone Hearth Trattoria</h1>
  <div class="person" style="left:0;top:124px"><b>Paolo Ferrante</b><span>Owner &amp; CEO</span><em>paolo@margueritestrattoria.com</em></div>
  <div class="person" style="left:96px;top:124px"><b>Marco Bellini</b><span>Owner, Silent Partner</span><em>marco@margueritestrattoria.com</em></div>
  <svg class="abs" style="left:178px;top:22px" width="170" height="170" viewBox="0 0 170 170" aria-hidden="true"><circle cx="92" cy="80" r="72" fill="none" stroke="#fff" stroke-opacity=".5" stroke-width="1.2"/></svg>
  <div class="photo" role="img" aria-label="Photo of a whole cheese pizza in a brick oven kitchen" style="left:236px;top:52px;width:88px;height:88px;border-radius:50%;box-shadow:0 3px 8px rgba(0,0,0,.2);background:radial-gradient(circle at 48% 52%,#e9b456 0%,#d28d3a 45%,#8a7765 75%,#5f5d60 100%)"></div>
  <div class="photo" role="img" aria-label="Small photo of a tomato pizza" style="left:214px;top:38px;width:40px;height:40px;border-radius:50%;border:2px solid var(--white);box-shadow:0 2px 5px rgba(0,0,0,.2);background:radial-gradient(circle,#e2673f,#c9853c 70%,#b9803f)"></div>
  <div class="photo" role="img" aria-label="Small photo of a pizza with greens" style="left:226px;top:120px;width:40px;height:40px;border-radius:50%;border:2px solid var(--white);box-shadow:0 2px 5px rgba(0,0,0,.2);background:radial-gradient(circle,#7f9a3f,#a8a04a 60%,#d2a85a)"></div>
</section>

<!-- Row 2 -->
<section class="slide c1 r2">
  <div class="photo" role="img" aria-label="Photo of the restaurant storefront sign" style="left:36px;top:50px;width:115px;height:91px;background:linear-gradient(180deg,#d8c7b1 0%,#cdbca6 55%,#4b8466 74%,#2e5f46 100%)"></div>
  <div class="rule" style="left:166px;top:50px"></div>
  <h2 class="h-title" style="left:166px;top:53px;font-size:12.5px">About Us</h2>
  <p class="body-text abs" style="left:166px;top:73px;width:152px">Marguerite's Stone Hearth Trattoria is a quality casual restaurant offering freshly cooked, delicious pizzas made with carefully crafted homemade sauce and dough. We prioritize customer satisfaction and provide lightning-quick food times, making us a top choice for takeout and delivery.</p>
  <div class="stat stat--navy" style="left:167px;top:110px;width:57px;height:29px;padding-top:5px"><b>+$265K</b><span>Our Sales</span></div>
  <div class="stat stat--card" style="left:232px;top:110px;width:55px;height:29px;padding-top:5px"><b>&gt;50</b><span>Location Point</span></div>
  <div class="footer-edge"></div><p class="footer-brand">Marguerite's</p>
  <div class="footer-bar"><span>margueritestrattoria.com</span><span>page | 4</span></div>
</section>

<section class="slide c2 r2">
  <div class="rule" style="left:165px;top:25px"></div>
  <h2 class="h-title" style="left:0;right:0;top:28px;text-align:center">Our Vision</h2>
  <div class="vision-box">Our vision is to become the go-to destination for exceptional pizza experiences, known for our quality ingredients and outstanding service.</div>
  <div class="footer-edge"></div><p class="footer-brand">Marguerite's</p>
  <div class="footer-bar"><span>margueritestrattoria.com</span><span>page | 5</span></div>
</section>

<section class="slide c3 r2">
  <div class="rule" style="left:165px;top:25px"></div>
  <h2 class="h-title" style="left:0;right:0;top:28px;text-align:center">Our Mission</h2>
  <div class="rule" style="left:170px;top:67px;width:6px;height:.8px"></div>
  <p class="mission-text">Our mission is to delight customers with every bite and create memorable<br>moments through our delicious pizzas.</p>
  <div class="stat stat--card" style="left:107px;top:123px;width:64px;height:31px"></div>
  <div class="stat" style="left:34px;top:128px;width:50px"><b>+$265K</b><span>Our Sales</span></div>
  <div class="stat" style="left:114px;top:128px;width:50px"><b>&gt;50</b><span>Location Point</span></div>
  <div class="stat" style="left:189px;top:128px;width:50px"><b>&gt;32</b><span>Worker</span></div>
  <div class="stat" style="left:263px;top:128px;width:50px"><b>5</b><span>Start</span></div>
  <div class="footer-edge"></div><p class="footer-brand">Marguerite's</p>
  <div class="footer-bar"><span>margueritestrattoria.com</span><span>page | 6</span></div>
</section>

<!-- Row 3 -->
<section class="slide c1 r3">
  <div class="rule" style="left:165px;top:25px"></div>
  <h2 class="h-title" style="left:0;right:0;top:28px;text-align:center">The Market Opportunity</h2>
  <svg class="abs" style="left:34px;top:54px" width="100" height="100" viewBox="0 0 100 100" aria-hidden="true"><circle cx="50" cy="50" r="48" fill="none" stroke="#efe4c4" stroke-width=".8"/></svg>
  <div class="photo" role="img" aria-label="Golden circle behind a cheese pizza photo" style="left:41px;top:62px;width:86px;height:86px;border-radius:50%;background:var(--gold)"></div>
  <div class="photo" role="img" aria-label="Photo of a whole cheese pizza" style="left:21px;top:80px;width:122px;height:55px;border-radius:50%;box-shadow:0 3px 6px rgba(0,0,0,.15);background:radial-gradient(ellipse at 50% 45%,#f4c55a 0%,#e6a13d 55%,#cf8a3b 85%,#c7c2b8 100%)"></div>
  <div class="card" style="left:153px;top:53px;width:169px;height:111px;padding:7px 8px">
    <div class="list-item body-text"><h4>Overview of the Pizza Industry:</h4><p>The pizza industry is a thriving and highly popular segment of the food service market. With a diverse range of customers and a growing demand for convenient dining options, the industry presents significant growth opportunities.</p></div>
    <div class="list-item body-text"><h4>Market Size and Growth Potential:</h4><p>The pizza industry generates billions of dollars in revenue each year, and its potential for growth remains strong. As we expand our presence, we tap into the appetite for quality pizza and the rising trend of takeout and delivery.</p></div>
    <div class="list-item body-text"><h4>Target Audience and Customer Demographics:</h4><p>Our target audience spans individuals from 18 to 80 years old, both male and female, with a focus on the middle-class demographic. A menu for diverse tastes draws a broad customer base.</p></div>
  </div>
  <div class="footer-edge"></div><p class="footer-brand">Marguerite's</p>
  <div class="footer-bar"><span>margueritestrattoria.com</span><span>page | 7</span></div>
</section>

<section class="slide c2 r3">
  <div class="rule" style="left:29px;top:19px"></div>
  <h2 class="h-title" style="left:31px;top:22px">Unique Selling Proposition</h2>
  <div class="card" style="left:42px;top:44px;width:165px;height:60px;padding:6px 7px 0 13px">
    <p class="sub">What Sets Our Pizzeria Apart</p>
    <p class="body-text">At Marguerite's Stone Hearth Trattoria, our commitment to excellence sets us apart. We pride ourselves on carefully crafted proprietary recipes for our homemade sauce and dough, resulting in exceptional product quality. Our small, profitable menu ensures consistency and lightning-quick food times.</p>
  </div>
  <div class="icon-dot" style="left:29px;top:64px"><svg width="10" height="10" viewBox="0 0 10 10" fill="none" stroke="#fff" stroke-width=".8"><circle cx="5" cy="5" r="3"/><path d="M1 2v3M9 2v6"/></svg></div>
  <div class="card" style="left:42px;top:112px;width:165px;height:56px;padding:6px 7px 0 13px">
    <p class="sub">Key Differentiators and Competitive Advantages</p>
    <p class="body-text">Our ability to make anything on our menu in minutes, coupled with convenient ordering options including mobile ordering, delivery, takeout and in-person dining, sets us apart. We prioritize our customers' fast-paced needs and the best quality product and service.</p>
  </div>
  <div class="icon-dot" style="left:29px;top:130px"><svg width="9" height="9" viewBox="0 0 10 10" fill="none" stroke="#fff" stroke-width=".8"><path d="M2 5h2v4H2zM4 5l2-4c1 0 1 1 1 2v1h2l-1 5H4"/></svg></div>
  <div class="photo" role="img" aria-label="Photo of two chefs with pizzas in the kitchen" style="left:217px;top:0;width:96px;height:52px;background:linear-gradient(180deg,#e1ddd6 0%,#b9aa98 45%,#6f6a66 70%,#c97f3f 88%,#e0a15a)"></div>
  <div class="photo" role="img" aria-label="Online ordering promo with phone app and pasta dish" style="left:217px;top:57px;width:96px;height:112px;background:linear-gradient(165deg,#0f0f10 0%,#1a1a1b 55%,#6e3322 78%,#c88d55 100%)"></div>
  <div class="footer-edge"></div><p class="footer-brand">Marguerite's</p>
  <div class="footer-bar"><span>margueritestrattoria.com</span><span>page | 8</span></div>
</section>

<section class="slide c3 r3">
  <div class="photo" role="img" aria-label="Pale yellow panel behind a pizza" style="left:31px;top:0;width:101px;height:120px;border-radius:0 0 14px 14px;background:linear-gradient(180deg,var(--cream),#fbf7e2)"></div>
  <div class="photo" role="img" aria-label="Photo of a pizza topped with arugula and prosciutto" style="left:20px;top:36px;width:124px;height:124px;border-radius:50%;box-shadow:0 4px 10px rgba(0,0,0,.18);background:radial-gradient(circle,#5f8a34 0%,#7d9a44 45%,#b9a85e 68%,#e6cf8e 85%,#d9b774 100%)"></div>
  <div class="rule" style="left:180px;top:33px"></div>
  <h2 class="h-title" style="left:180px;top:36px;font-size:12.5px">Business Model</h2>
  <div class="abs" style="left:182px;top:57px;width:140px">
    <div class="list-item body-text sq"><h4>Revenue Streams</h4><p>Our revenue streams include dine-in, takeout, delivery and catering services. By offering multiple avenues for customers to enjoy our pizzas, we maximize revenue and cater to various preferences.</p></div>
    <div class="list-item body-text sq"><h4>Pricing Strategy and Menu Overview</h4><p>We have carefully priced our menu to ensure maximum profitability while delivering value. Our menu offers a selected range of signature pies, including the Rosa, Verde and Classic, each a delightful experience.</p></div>
    <div class="list-item body-text sq"><h4>Operating Hours and Location(s)</h4><p>Our pizzeria operates from 11 am to 9 pm, catering to lunch and dinner crowds. Our flagship is at 18 Orchard Lane, Suite 4, Millbrook, NY 12545, a convenient and accessible location.</p></div>
  </div>
  <div class="footer-edge"></div><p class="footer-brand">Marguerite's</p>
  <div class="footer-bar"><span>margueritestrattoria.com</span><span>page | 9</span></div>
</section>

</body>
</html>
```